Business Card design for construction company

I would like a business card design for a construction company - Harlow Constructions. I have attached the ai logo file for use. I would like the card to be very smart and clean and incorporate only white and the two colours in the logo. I would like the card to have two sides. One side can just have the logo, the other with the relevant information.

Target Market(s)

Building and Construction Clients

Industry/Entity Type

Business

Contact Information for Business Card

Name: Tom Pardoe
Company: Harlow Constructions Pty Limited
Address: 14 Mallee Crescent Carrow Vale 2093
Phone: 0427 531 068
Email: tomp@harlowbuild-example.com.au

Font styles to use
Serif
Sans Serif

Requirements
Must have
• Details noted above
• Logo as provided
• Colours as in logo
• Square edges
• A font that compliments the logo
Should not have
• Any colour other than white and those in logo
• Rounded edges

```html
<!DOCTYPE html>
<html lang="en">
<head>
<meta charset="utf-8">
<title>Harlow Constructions – Business Card</title>
<link href="https://fonts.googleapis.com/css2?family=Exo+2:wght@300;400;600;700&display=swap" rel="stylesheet">
<style>
  :root {
    --brand-blue: #3a9fe0;
    --brand-blue-deep: #2f8fd2;
    --charcoal: #3d3f44;
    --text-grey: #4a4c52;
    --card-white: #f4f5f7;
    --card-shade: #e6e8eb;
    --backdrop: #dcdfe3;
  }
  * { box-sizing: border-box; margin: 0; padding: 0; }
  html, body { width: 1200px; height: 800px; overflow: hidden; }
  body {
    background: var(--backdrop);
    font-family: "Exo 2", "Helvetica Neue", Arial, sans-serif;
    position: relative;
  }
  .card {
    position: absolute;
    width: 510px;
    height: 292px;
    background: radial-gradient(circle at 45% 40%, #ffffff 0%, var(--card-white) 55%, var(--card-shade) 100%);
    overflow: hidden;
    box-shadow: 0 6px 18px rgba(0,0,0,0.12);
  }
  .card-front { left: 60px; top: 254px; }
  .card-back { left: 630px; top: 254px; }

  /* Front */
  .front-tab {
    position: absolute;
    width: 34px;
    height: 96px;
    background: var(--brand-blue);
  }
  .front-tab--top { right: 0; top: 30px; border-radius: 34px 0 0 34px; }
  .front-tab--bottom { left: 0; bottom: 40px; border-radius: 0 34px 34px 0; }
  .front-wordmark {
    position: absolute;
    left: 0; right: 0; top: 118px;
    text-align: center;
    font-weight: 400;
    font-size: 30px;
    letter-spacing: 3px;
    text-transform: uppercase;
    color: var(--charcoal);
  }
  .front-address {
    position: absolute;
    right: 40px; bottom: 34px;
    font-size: 14px;
    font-weight: 400;
    color: var(--text-grey);
  }

  /* Back */
  .back-strip {
    position: absolute;
    left: 0; top: 0;
    width: 112px; height: 100%;
    background: linear-gradient(180deg, var(--brand-blue) 0%, var(--brand-blue-deep) 100%);
  }
  .icon-tab {
    position: absolute;
    left: 96px; top: 134px;
    width: 50px; height: 130px;
    background: var(--charcoal);
    border-radius: 0 22px 22px 0;
    display: flex;
    flex-direction: column;
    justify-content: space-evenly;
    align-items: center;
    padding-left: 8px;
  }
  .icon-dot {
    width: 24px; height: 24px;
    border-radius: 50%;
    background: var(--brand-blue);
    display: flex; align-items: center; justify-content: center;
  }
  .icon-dot svg { width: 14px; height: 14px; }
  .person {
    position: absolute;
    left: 174px; top: 46px;
  }
  .person-name {
    font-size: 24px;
    font-weight: 700;
    color: var(--charcoal);
    line-height: 1.05;
  }
  .person-name .surname { color: var(--brand-blue); }
  .person-title {
    font-size: 18px;
    font-weight: 400;
    color: var(--charcoal);
  }
  .contact-list {
    position: absolute;
    left: 174px; top: 160px;
    list-style: none;
    font-size: 15px;
    color: var(--charcoal);
    line-height: 28px;
  }
  .company-vertical {
    position: absolute;
    right: 14px; top: 50%;
    transform: translate(50%, -50%) rotate(90deg);
    transform-origin: center;
    white-space: nowrap;
    font-size: 15px;
    font-weight: 700;
    color: var(--charcoal);
    margin-right: 10px;
  }
</style>
</head>
<body>

<section class="card card-front" aria-label="Business card front">
  <div class="front-tab front-tab--top"></div>
  <div class="front-tab front-tab--bottom"></div>
  <div class="front-wordmark">Harlow Constructions</div>
  <div class="front-address">14 Mallee Crescent, Carrow Vale 2093</div>
</section>

<section class="card card-back" aria-label="Business card back">
  <div class="back-strip"></div>
  <div class="icon-tab">
    <span class="icon-dot">
      <svg viewBox="0 0 24 24" fill="#fff"><path d="M6.6 10.8a15.1 15.1 0 0 0 6.6 6.6l2.2-2.2a1 1 0 0 1 1-.25 11.4 11.4 0 0 0 3.6.57 1 1 0 0 1 1 1V20a1 1 0 0 1-1 1A17 17 0 0 1 3 4a1 1 0 0 1 1-1h3.5a1 1 0 0 1 1 1c0 1.25.2 2.45.57 3.57a1 1 0 0 1-.25 1z"/></svg>
    </span>
    <span class="icon-dot">
      <svg viewBox="0 0 24 24" fill="#fff"><path d="M3 6h18v12H3z" fill="none" stroke="#fff" stroke-width="2"/><path d="M3 6l9 7 9-7" fill="none" stroke="#fff" stroke-width="2"/></svg>
    </span>
    <span class="icon-dot">
      <svg viewBox="0 0 24 24" fill="none" stroke="#fff" stroke-width="2"><circle cx="12" cy="12" r="9"/><path d="M3 12h18M12 3c3 3.5 3 14.5 0 18M12 3c-3 3.5-3 14.5 0 18"/></svg>
    </span>
  </div>

  <div class="person">
    <div class="person-name">Tom <span class="surname">Pardoe</span></div>
    <div class="person-title">Director</div>
  </div>

  <ul class="contact-list">
    <li>0427 531 068</li>
    <li>tomp@harlowbuild-example.com.au</li>
    <li>www.harlowbuild-example.com.au</li>
  </ul>

  <div class="company-vertical">Harlow Constructions Pty Limited</div>
</section>

</body>
</html>
```